RMT Electrical Business Card Design

Have a logo to use, just looking for design around this, would like green theme, would like symbols in place of phone, fax, email etc.

Business

Contact Information for Business Card

RMT Electrical, Simon Ashcroft, simon@rmtelectrical-example.com.au, www.rmtelectrical-example.com.au, mobile 0412 555 019, phone (07) 3555 0142, fax (07) 3555 0142, facebook and linkedin
addresses

```html
<!DOCTYPE html>
<html lang="en">
<head>
<meta charset="utf-8">
<title>RMT Electrical – Business Card</title>
<link rel="stylesheet" href="https://fonts.googleapis.com/css2?family=Questrial&family=Montserrat:wght@700;800&display=swap">
<style>
  :root {
    --page: #d9d9d9;
    --card: #f4f4f4;
    --paper: #ececec;
    --band: #9a9a9a;
    --green: #3cb54a;
    --ink: #1c1c1c;
    --black: #161616;
    --icon: #6d6d6d;
    --web: #e8e8e8;
    --shadow: rgba(0,0,0,0.22);
  }
  * { box-sizing: border-box; margin: 0; padding: 0; }
  html, body { width: 1200px; height: 1000px; overflow: hidden; }
  body {
    background: var(--page);
    font-family: "Questrial", "Century Gothic", sans-serif;
    color: var(--ink);
    position: relative;
  }
  .card {
    position: absolute;
    left: 250px;
    width: 700px;
    height: 400px;
    background: var(--card);
    box-shadow: 0 8px 24px var(--shadow);
    overflow: hidden;
  }
  .card--front { top: 60px; }
  .card--back { top: 540px; }

  /* Front */
  .front-brand {
    position: absolute;
    inset: 0;
    display: flex;
    flex-direction: column;
    align-items: center;
    justify-content: center;
    gap: 26px;
  }
  .brand-dot {
    width: 150px; height: 150px;
    border-radius: 50%;
    background: var(--green);
    flex: none;
  }
  .brand-name {
    font-size: 76px;
    letter-spacing: 1px;
    color: var(--ink);
    line-height: 1;
    white-space: nowrap;
  }

  /* Back */
  .back-shapes { position: absolute; inset: 0; width: 700px; height: 400px; }
  .back-brand {
    position: absolute;
    top: 28px; left: 150px;
    display: flex; align-items: center; gap: 18px;
  }
  .back-brand .brand-dot { width: 62px; height: 62px; }
  .back-brand .brand-name { font-size: 54px; }

  .social {
    position: absolute;
    left: 34px; top: 196px;
    color: var(--ink);
  }
  .social-title {
    font-family: "Montserrat", sans-serif;
    font-weight: 700;
    font-size: 17px;
    margin-bottom: 6px;
  }
  .social-row {
    display: flex; align-items: center; gap: 8px;
    font-size: 20px; line-height: 28px;
  }
  .social-dot {
    width: 20px; height: 20px; border-radius: 50%;
    background: var(--icon);
  }

  .contact {
    position: absolute;
    right: 22px; top: 180px;
    text-align: right;
  }
  .contact-name {
    font-family: "Montserrat", sans-serif;
    font-weight: 800;
    font-size: 21px;
    line-height: 26px;
    margin-right: 38px;
  }
  .contact-row {
    display: flex; align-items: center; justify-content: flex-end;
    gap: 10px;
    font-size: 19px;
    line-height: 28px;
    height: 30px;
    white-space: nowrap;
  }
  .contact-row--email { font-size: 18px; }
  .contact-icon {
    width: 26px; height: 26px;
    border-radius: 50%;
    background: var(--icon);
    display: flex; align-items: center; justify-content: center;
    flex: none;
  }
  .contact-icon svg { width: 15px; height: 15px; }

  .website {
    position: absolute;
    left: 150px; top: 341px;
    font-size: 22px;
    line-height: 30px;
    color: var(--web);
    letter-spacing: 0.5px;
    white-space: nowrap;
  }
  .website strong { color: var(--green); font-weight: 400; }
</style>
</head>
<body>

<section class="card card--front" aria-label="Business card front">
  <div class="front-brand">
    <div class="brand-dot"></div>
    <div class="brand-name">RMT Electrical</div>
  </div>
</section>

<section class="card card--back" aria-label="Business card back">
  <svg class="back-shapes" viewBox="0 0 700 400" preserveAspectRatio="none">
    <rect width="700" height="400" fill="var(--paper)"/>
    <path d="M0 130 Q350 104 700 160 L700 400 L0 400 Z" fill="var(--band)"/>
    <path d="M0 144 Q350 118 700 174 L700 400 L0 400 Z" fill="var(--green)"/>
    <rect x="0" y="334" width="700" height="46" fill="var(--black)"/>
    <rect x="0" y="339" width="140" height="2" fill="var(--green)"/>
    <rect x="560" y="373" width="140" height="2" fill="var(--green)"/>
    <rect x="0" y="380" width="700" height="20" fill="var(--card)"/>
  </svg>

  <div class="back-brand">
    <div class="brand-dot"></div>
    <div class="brand-name">RMT Electrical</div>
  </div>

  <div class="social">
    <div class="social-title">Follow us on</div>
    <div class="social-row"><span class="social-dot"></span>rmtelectrical</div>
    <div class="social-row"><span class="social-dot"></span>simonashcroft</div>
  </div>

  <div class="contact">
    <div class="contact-name">Simon Ashcroft</div>
    <div class="contact-row contact-row--email">simon@rmtelectrical-example.com.au
      <span class="contact-icon" aria-label="Email"><svg viewBox="0 0 16 16"><rect x="1.5" y="3.5" width="13" height="9" fill="none" stroke="#fff" stroke-width="1.4"/><path d="M1.5 3.5 L8 9 L14.5 3.5" fill="none" stroke="#fff" stroke-width="1.4"/></svg></span>
    </div>
    <div class="contact-row">0412 555 019
      <span class="contact-icon" aria-label="Mobile"><svg viewBox="0 0 16 16"><rect x="4.5" y="1.5" width="7" height="13" rx="1.2" fill="none" stroke="#fff" stroke-width="1.4"/><circle cx="8" cy="12" r="0.9" fill="#fff"/></svg></span>
    </div>
    <div class="contact-row">(07) 3555 0142
      <span class="contact-icon" aria-label="Phone"><svg viewBox="0 0 16 16"><path d="M2 6 Q8 1 14 6 L12 8 L10 6.5 L6 6.5 L4 8 Z" fill="#fff"/><rect x="4" y="9" width="8" height="5" rx="1" fill="#fff"/></svg></span>
    </div>
    <div class="contact-row">(07) 3555 0142
      <span class="contact-icon" aria-label="Fax"><svg viewBox="0 0 16 16"><rect x="5" y="1.5" width="7" height="5" fill="none" stroke="#fff" stroke-width="1.3"/><rect x="2" y="6.5" width="12" height="8" rx="1" fill="#fff"/><rect x="5" y="9" width="6" height="1.2" fill="#6d6d6d"/><rect x="5" y="11.4" width="6" height="1.2" fill="#6d6d6d"/></svg></span>
    </div>
  </div>

  <div class="website">www.<strong>rmtelectrical-example</strong>.com.au</div>
</section>

</body>
</html>
```